Creative Brief
business card QV HAIR CARE
QV HAIR CARE
Bright & Fun-filled
DORIAN FELKOSTA
PO Box 5817 WILLOWMERE
CA 90478
df@qvhaircare-example.com
qvhaircare-example.com
current logo
tire tracks

```html
<!DOCTYPE html>
<html lang="en">
<head>
<meta charset="utf-8">
<title>QV Hair Care Stationery</title>
<link href="https://fonts.googleapis.com/css2?family=Michroma&family=Great+Vibes&family=Roboto:wght@400&display=swap" rel="stylesheet">
<style>
:root{
  --bg:#ececec;
  --paper:#ffffff;
  --green:#8cc63e;
  --green-deep:#6aa82a;
  --green-light:#d4ec9a;
  --logo-grey:#8a8a8a;
  --ink:#777;
  --faint:#f1f6e6;
}
*{margin:0;padding:0;box-sizing:border-box}
html,body{width:1200px;height:902px;overflow:hidden;background:var(--bg)}
.canvas{position:relative;width:1200px;height:902px;background:radial-gradient(ellipse at center,#f7f7f7 0%,#e3e3e3 100%)}
.sheet{position:absolute;background:var(--paper);box-shadow:0 2px 6px rgba(0,0,0,.22);overflow:hidden}
.brand{font-family:"Michroma",sans-serif;color:var(--logo-grey);letter-spacing:1px;white-space:nowrap}
.footer{position:absolute;left:0;right:0;font-family:"Roboto",sans-serif;font-size:6px;color:var(--ink);text-align:center;white-space:nowrap}
.rule{position:absolute;left:0;right:0;height:3px;background:linear-gradient(90deg,var(--green-light),var(--green),var(--green-light))}
.band{position:absolute;left:0;right:0;top:0;background:linear-gradient(90deg,var(--green-light),var(--green) 40%,var(--green-deep))}

/* business cards */
.card-front{left:224px;top:59px;width:174px;height:68px}
.card-front .brand{position:absolute;left:10px;top:14px;font-size:11px}
.card-front .contact{position:absolute;left:10px;bottom:8px;font-family:"Roboto",sans-serif;font-size:5px;color:var(--ink);line-height:1.4}
.card-front .band{top:auto;bottom:0;height:4px}
.card-back{left:410px;top:59px;width:176px;height:68px;background:linear-gradient(135deg,var(--green-light),var(--green) 50%,var(--green-deep))}
.card-back .brand{position:absolute;left:22px;top:26px;font-size:12px;color:#fff}

/* letterhead */
.letterhead{left:600px;top:83px;width:542px;height:546px}
.letterhead .band{height:10px}
.letterhead .brand{position:absolute;right:60px;top:40px;font-size:22px}
.letterhead .watermark{position:absolute;right:20px;top:220px;font-family:"Michroma",sans-serif;font-size:70px;color:var(--faint);white-space:nowrap}
.letterhead .footer{bottom:18px}
.letterhead .rule{bottom:8px}

/* envelope */
.envelope{left:224px;top:176px;width:362px;height:195px}
.envelope svg{position:absolute;left:0;top:0}
.envelope .brand{position:absolute;left:0;right:0;top:14px;text-align:center;font-size:16px;color:#fff}
.envelope .footer{bottom:16px}
.envelope .rule{bottom:6px}

/* DL card */
.dl{left:334px;top:378px;width:427px;height:190px}
.dl .band{height:12px}
.dl .brand{position:absolute;left:0;right:0;top:80px;text-align:center;font-size:18px}
.dl .footer{bottom:20px}
.dl .rule{bottom:10px}

/* slip */
.slip{left:207px;top:585px;width:379px;height:191px}
.slip .band{height:14px}
.slip .brand{position:absolute;left:130px;top:80px;font-size:18px}
.slip .rule{bottom:12px}

/* compliments */
.compliments{left:471px;top:639px;width:400px;height:190px}
.compliments svg{position:absolute;left:0;top:0}
.compliments .brand{position:absolute;left:0;right:0;top:14px;text-align:center;font-size:15px;color:#fff}
.compliments .script{position:absolute;left:0;right:0;top:92px;text-align:center;font-family:"Great Vibes",cursive;font-size:30px;color:var(--green)}
.compliments .footer{bottom:18px}
.compliments .rule{bottom:8px}
</style>
</head>
<body>
<div class="canvas">

  <div class="sheet card-front">
    <div class="brand">QV HAIR CARE</div>
    <div class="contact">DORIAN FELKOSTA<br>T 818 555 0142 · df@qvhaircare-example.com</div>
    <div class="band"></div>
  </div>

  <div class="sheet card-back">
    <div class="brand">QV HAIR CARE</div>
  </div>

  <div class="sheet letterhead">
    <div class="band"></div>
    <div class="watermark" aria-hidden="true">QV HAIR CARE</div>
    <div class="brand">QV HAIR CARE</div>
    <div class="footer">PO Box 5817 WILLOWMERE CA 90478 &nbsp;|&nbsp; T 818 555 0142 &nbsp;|&nbsp; df@qvhaircare-example.com &nbsp;|&nbsp; qvhaircare-example.com</div>
    <div class="rule"></div>
  </div>

  <div class="sheet envelope">
    <svg width="362" height="80" viewBox="0 0 362 80" aria-hidden="true">
      <defs><linearGradient id="flapA" x1="0" x2="1"><stop offset="0" stop-color="#d4ec9a"/><stop offset=".5" stop-color="#8cc63e"/><stop offset="1" stop-color="#6aa82a"/></linearGradient></defs>
      <path d="M0 0H362V40Q181 90 0 40Z" fill="url(#flapA)"/>
    </svg>
    <div class="brand">QV HAIR CARE</div>
    <div class="footer">PO Box 5817 WILLOWMERE CA 90478 &nbsp;|&nbsp; T 818 555 0142 &nbsp;|&nbsp; df@qvhaircare-example.com &nbsp;|&nbsp; qvhaircare-example.com</div>
    <div class="rule"></div>
  </div>

  <div class="sheet dl">
    <div class="band"></div>
    <div class="brand">QV HAIR CARE</div>
    <div class="footer">PO Box 5817 WILLOWMERE CA 90478 &nbsp;|&nbsp; T 818 555 0142 &nbsp;|&nbsp; df@qvhaircare-example.com &nbsp;|&nbsp; qvhaircare-example.com</div>
    <div class="rule"></div>
  </div>

  <div class="sheet slip">
    <div class="band"></div>
    <div class="brand">QV HAIR CARE</div>
    <div class="rule"></div>
  </div>

  <div class="sheet compliments">
    <svg width="400" height="75" viewBox="0 0 400 75" aria-hidden="true">
      <defs><linearGradient id="flapB" x1="0" x2="1"><stop offset="0" stop-color="#d4ec9a"/><stop offset=".5" stop-color="#8cc63e"/><stop offset="1" stop-color="#6aa82a"/></linearGradient></defs>
      <path d="M0 0H400V38Q200 85 0 38Z" fill="url(#flapB)"/>
    </svg>
    <div class="brand">QV HAIR CARE</div>
    <div class="script">With Compliments</div>
    <div class="footer">PO Box 5817 WILLOWMERE CA 90478 &nbsp;|&nbsp; df@qvhaircare-example.com &nbsp;|&nbsp; qvhaircare-example.com</div>
    <div class="rule"></div>
  </div>

</div>
</body>
</html>
```